Velmora Partners - website for real estate investment company

Create a bold, modern website that reflects Velmora’s success, professionalism, and credibility.
The design must stand out while maintaining a polished, corporate tone. (bold, but understated)
The client just created a new logo, and the website design must be in sync with the logo design. Information about the logo colors, fonts, and message are in the attached design brief.
Updates

Target Market(s)

b2b: banks, brokers, institutional partners, vendors, and property sellers.

Industry/Entity Type

real estate investment company

Number of Pages Required

1 page

Font styles to use
Sans Serif

Colors

Designer to choose colors to be used in the design.

Requirements
Must have
• 1. homepage design (psd) 2. a top banner image (psd) for a default inner page
Nice to have
• please see attached design brief
Should not have

```html
<!DOCTYPE html>
<html lang="en">
<head>
<meta charset="UTF-8">
<title>Velmora Partners</title>
<link href="https://fonts.googleapis.com/css2?family=Barlow+Semi+Condensed:wght@700&family=Poppins:wght@400;500;600&display=swap" rel="stylesheet">
<style>
:root{
  --red:#e01f2a;
  --ink:#3a3a3a;
  --black:#111;
  --white:#fff;
  --footer:#3b3b3d;
}
*{margin:0;padding:0;box-sizing:border-box}
html,body{width:1097px;height:1200px;overflow:hidden}
body{position:relative;font-family:'Poppins',sans-serif;background:var(--white)}
.hero{position:absolute;left:0;top:0;width:1097px;height:667px;
  background:linear-gradient(180deg,#c9c3cf 0%,#e9a7a0 14%,#f2a772 30%,#f5c154 44%,#f09a4e 55%,#8a5a6e 68%,#4a4660 82%,#2f3344 100%)}
.hero-city{position:absolute;right:0;top:0;width:1097px;height:667px;
  background:radial-gradient(ellipse 230px 560px at 760px 430px,rgba(40,55,85,.85),rgba(40,55,85,0) 70%)}
.brand{position:absolute;font-family:'Barlow Semi Condensed',sans-serif;font-weight:700;letter-spacing:1px}
.brand-top{left:101px;top:22px;font-size:38px;color:var(--ink)}
.nav{position:absolute;left:298px;top:34px;display:flex;gap:7px;font-size:12.5px;font-weight:500;color:var(--black)}
.nav span.sep{font-weight:600}
.btn-contact{position:absolute;left:868px;top:22px;width:125px;height:40px;background:var(--red);color:var(--white);font-size:13px;font-weight:600;display:flex;align-items:center;justify-content:center}
.headline{position:absolute;left:101px;top:134px;font-family:'Barlow Semi Condensed',sans-serif;font-weight:700;font-size:58px;line-height:61px;letter-spacing:1px}
.headline .l1{color:var(--ink)}
.headline .l2{color:var(--red)}
.headline .l3{color:var(--black)}
.intro{position:absolute;left:298px;top:279px;width:320px;font-size:11.2px;font-weight:500;line-height:24.3px;color:var(--black);text-transform:uppercase}
.play{position:absolute;left:150px;top:365px}
.btn-projects{position:absolute;left:297px;top:456px;width:170px;height:40px;background:var(--ink);color:var(--white);font-size:13px;font-weight:600;display:flex;align-items:center;justify-content:center}
.accent{position:absolute;left:895px;top:165px}
.stats{position:absolute;left:0;top:667px;width:1097px;height:243px;background:var(--red);color:var(--white)}
.stat{position:absolute;top:62px;width:240px;text-align:center}
.stat-num{font-size:34px;font-weight:500;line-height:40px}
.stat-label{font-size:12.5px;font-weight:500;line-height:22px;margin-top:12px;text-transform:uppercase}
.divider{position:absolute;top:20px;width:1px;height:185px;background:rgba(255,255,255,.45)}
.footer{position:absolute;left:0;top:910px;width:1097px;height:290px;
  background:linear-gradient(90deg,#4a4848 0%,#3d3c3d 35%,#363638 70%,#3a393b 100%)}
.brand-foot{left:102px;top:90px;font-size:44px;color:var(--white)}
.copyright{position:absolute;left:110px;top:164px;font-size:10px;color:var(--white)}
.connect{position:absolute;left:364px;top:32px;width:369px;text-align:center;color:var(--red);font-size:15px;font-weight:500}
.field{position:absolute;background:var(--white);font-size:8.5px;color:#666;padding:10px 15px;text-transform:uppercase}
.submit{position:absolute;left:364px;top:169px;width:369px;height:33px;background:var(--red);color:var(--white);font-size:9.5px;font-weight:600;display:flex;align-items:center;justify-content:center}
.contact-head{position:absolute;left:825px;top:97px;color:var(--red);font-size:12.5px;font-weight:500}
.contact-item{position:absolute;left:825px;display:flex;align-items:center;gap:8px;color:var(--white);font-size:13px;font-weight:500}
</style>
</head>
<body>
<section class="hero">
  <div class="hero-city" role="img" aria-label="Aerial photo of a city skyline at sunset with a tall glass office tower"></div>
  <div class="brand brand-top">VELMORA</div>
  <nav class="nav">
    <span>HOME</span><span class="sep">|</span><span>OUR STORY</span><span class="sep">|</span><span>INVESTMENT STRATEGY</span><span class="sep">|</span><span>WHAT SETS US APART</span><span class="sep">|</span><span>OUR PORTFOLIO</span>
  </nav>
  <div class="btn-contact">CONTACT US</div>
  <h1 class="headline"><div class="l1">EXPERIENCE</div><div class="l2">STRATEGY</div><div class="l3">VISION</div></h1>
  <p class="intro">Velmora Partners is a vertically integrated real estate investment firm with a proven four decade track record. We acquire, reposition, and operate high-performing assets across multiple sectors always with a focus on exceptional, risk-adjusted returns.</p>
  <svg class="play" width="64" height="64" viewBox="0 0 64 64"><circle cx="32" cy="32" r="32" fill="#000"/><path d="M25 21 L43 32 L25 43 Z" fill="#fff"/></svg>
  <div class="btn-projects">VIEW OUR PROJECTS</div>
  <svg class="accent" width="126" height="130" viewBox="0 0 126 130"><path d="M0 0 H126 L0 130 Z" fill="#e01f2a"/></svg>
</section>

<section class="stats">
  <div class="stat" style="left:148px"><div class="stat-num">1989</div><div class="stat-label">Founded</div></div>
  <div class="divider" style="left:398px"></div>
  <div class="stat" style="left:427px"><div class="stat-num">23,000+</div><div class="stat-label">Multifamily &amp;<br>Healthcare Units</div></div>
  <div class="divider" style="left:699px"></div>
  <div class="stat" style="left:705px"><div class="stat-num">$300+</div><div class="stat-label">Million invested in<br>renovations</div></div>
</section>

<footer class="footer" role="img" aria-label="Dimmed photo of business people in a meeting">
  <div class="brand brand-foot">VELMORA</div>
  <div class="copyright">Copyright@2025.All Rights Reserved</div>
  <div class="connect">CONNECT WITH US</div>
  <div class="field" style="left:364px;top:69px;width:181px;height:34px">Name</div>
  <div class="field" style="left:552px;top:69px;width:181px;height:34px">Email</div>
  <div class="field" style="left:364px;top:111px;width:369px;height:50px">Message</div>
  <div class="submit">SUBMIT</div>
  <div class="contact-head">CONTACT US</div>
  <div class="contact-item" style="top:123px">
    <svg width="9" height="13" viewBox="0 0 9 13"><path d="M4.5 0A4.5 4.5 0 0 0 0 4.5C0 8 4.5 13 4.5 13S9 8 9 4.5A4.5 4.5 0 0 0 4.5 0Zm0 6.3a1.8 1.8 0 1 1 0-3.6 1.8 1.8 0 0 1 0 3.6Z" fill="#fff"/></svg>
    <span>Aldenbrook, NJ</span>
  </div>
  <div class="contact-item" style="top:155px">
    <svg width="13" height="10" viewBox="0 0 13 10"><rect width="13" height="10" rx="1" fill="#fff"/><path d="M0.5 1 L6.5 5.5 L12.5 1" stroke="#3b3b3d" stroke-width="1.2" fill="none"/></svg>
    <span>info@velmorapartners.com</span>
  </div>
</footer>
</body>
</html>
```